Revamp of existing namecard

Existingly, i've got a namecard that i would like to retain the main design. but there are some changes in my company and i would need to do some amendments to it.

We are a money transfer and money exchange company.
I need 2 different types of name card.
1. For individual name cards
the front to put the following:
Company name and logo
English Name, Chinese Name appointment
Mobile Number, Email and Website.
2 License number under the logo and name

the back of the name card to put
8 address: 7 Singapore and 1 Hong Kong branch addresses
8 Mobile Number of the corresponding addresses.

We would like to retain the name card front design
the name card back design can change but color to retain.

2nd name card is generic name card
Front:
Company name and logo
Branch Mobile Number, Branch Address, Email and Website.

Industry/Entity Type

remittance and money exchange

Contact Information for Business Card

I need 2 different types of name card. 1. For individual name cards the front to put the following: Company name and logo English Name, Chinese Name appointment Mobile Number, Email and Website. 2 License number under the logo and name the back of the name card to put 8 address: 7 Singapore and 1 Hong Kong branch addresses 8 Mobile Number of the corresponding addresses. We would like to retain the name card front design the name card back design can change but color to retain. 2nd name card is generic name card Front: the front to put the following: Company name and logo Branch Mobile Number, Branch Address, Email and Website. 2 License number under the logo and name

Requirements
Must have
• I need 2 different types of name card. 1. For individual name cards the front to put the following: Company name and logo English Name, Chinese Name appointment Mobile Number, Email and Website. 2 License number under the logo and name the back of the name card to put 8 address: 7 Singapore and 1 Hong Kong branch addresses 8 Mobile Number of the corresponding addresses. We would like to retain the name card front design the name card back design can change but color to retain. 2nd name card is generic name card Front: the front to put the following: Company name and logo Branch Mobile Number, Branch Address, Email and Website. 2 License number under the logo and name
Nice to have
• use back color code

```html
<!DOCTYPE html>
<html lang="en">
<head>
<meta charset="utf-8">
<title>Velora Name Card</title>
<link rel="stylesheet" href="https://fonts.googleapis.com/css2?family=Montserrat:wght@400;500;600;700;800&family=Noto+Sans+TC:wght@700&display=swap">
<style>
  :root{
    --bg:#e7e5e2;
    --card-white:#f7f7f7;
    --navy:#1f2d39;
    --ink:#22313d;
    --teal:#5fb6c4;
    --map:#e6e8ea;
    --muted:#4a5a66;
  }
  *{box-sizing:border-box;margin:0;padding:0}
  html,body{width:1200px;height:900px;overflow:hidden;background:var(--bg);font-family:'Montserrat',sans-serif;color:var(--ink)}
  .canvas{position:relative;width:1200px;height:900px}
  .card{position:absolute;left:250px;width:700px;height:400px;border-radius:22px;overflow:hidden;box-shadow:0 10px 30px rgba(0,0,0,.18)}
  .card-front{top:35px;background:var(--card-white)}
  .card-back{top:465px;background:var(--navy)}

  /* front */
  .world-map{position:absolute;left:140px;top:40px;width:480px;height:240px;border-radius:40px;background:radial-gradient(ellipse at center,var(--map) 0%,rgba(230,232,234,0) 70%)}
  .brand{position:absolute;left:40px;top:52px;display:flex;align-items:center;gap:14px}
  .brand-mark{width:46px;height:46px;background:var(--teal);border-radius:6px}
  .brand-name{font-size:38px;font-weight:700;letter-spacing:2px;line-height:1;color:var(--ink)}
  .brand-sub{font-size:8.5px;font-weight:600;letter-spacing:2.2px;margin-top:5px;border-bottom:1px solid var(--teal);padding-bottom:3px}
  .brand-license{font-size:8.5px;letter-spacing:1.5px;text-align:center;margin-top:3px}
  .tab{position:absolute;right:0;top:70px;width:22px;height:58px;background:var(--teal);border-radius:6px 0 0 6px}
  .person{position:absolute;right:52px;top:110px;text-align:right}
  .person-name{font-size:30px;font-weight:800;color:var(--ink)}
  .person-name .zh{font-family:'Noto Sans TC',sans-serif;font-size:26px;margin-left:6px}
  .person-role{font-size:15px;font-weight:500;color:var(--teal);margin-top:2px}
  .person-license{font-size:12px;color:var(--teal);margin-top:2px}
  .person-license b{color:var(--ink);font-weight:600}
  .divider{position:absolute;left:40px;right:52px;top:236px;height:1.5px;background:var(--teal)}
  .contacts{position:absolute;left:40px;top:258px;list-style:none}
  .contacts li{display:flex;align-items:center;gap:10px;font-size:16px;font-weight:500;letter-spacing:1.2px;height:26px}
  .contacts svg{width:16px;height:16px;flex:none}
  .address{position:absolute;right:52px;top:270px;text-align:right;font-size:15px;font-weight:500;line-height:1.55;letter-spacing:.6px}

  /* back */
  .back-frame{position:absolute;inset:16px;border:2px solid var(--teal);display:grid;grid-template-columns:1fr 170px 1fr}
  .branch-col{display:grid;grid-template-rows:repeat(4,1fr)}
  .branch{border-bottom:2px solid var(--teal);padding:12px 14px;color:#fff;font-size:12px;line-height:1.45;font-weight:500}
  .branch:last-child{border-bottom:none}
  .branch-phone{display:flex;align-items:center;gap:8px;font-size:13px;font-weight:600}
  .branch-phone svg{width:13px;height:13px}
  .back-brand{border-left:2px solid var(--teal);border-right:2px solid var(--teal);display:flex;flex-direction:column;align-items:center;justify-content:center;gap:12px;color:#fff}
  .back-brand .brand-mark{width:44px;height:44px}
  .back-brand .brand-name{color:#fff;font-size:30px}
  .back-brand .brand-sub{color:#fff;font-size:7px;letter-spacing:1.4px;border:none;text-align:center}
</style>
</head>
<body>
<main class="canvas">

  <section class="card card-front">
    <div class="world-map" role="img" aria-label="Faint dotted world map background"></div>
    <div class="brand">
      <span class="brand-mark"></span>
      <div>
        <div class="brand-name">VELORA</div>
        <div class="brand-sub">REMITTANCE AND MONEY EXCHANGE</div>
        <div class="brand-license">License :- 1234567</div>
      </div>
    </div>
    <span class="tab"></span>
    <div class="person">
      <div class="person-name">Marcus Lee<span class="zh">(李明遠)</span></div>
      <div class="person-role">Director of Business Development</div>
      <div class="person-license">License :- <b>1234567</b></div>
    </div>
    <div class="divider"></div>
    <ul class="contacts">
      <li><svg viewBox="0 0 16 16"><rect x="4" y="1" width="8" height="14" rx="1.5" fill="none" stroke="#5fb6c4" stroke-width="1.5"/></svg>+852 5550 1234</li>
      <li><svg viewBox="0 0 16 16"><path d="M3 2l3 0 1 3-2 1.5c1 2 2.5 3.5 4.5 4.5L11 9l3 1v3c-6 1-12-5-11-11z" fill="#5fb6c4"/></svg>+852 5550 5678</li>
      <li><svg viewBox="0 0 16 16"><rect x="1" y="3" width="14" height="10" fill="#5fb6c4"/><path d="M1 3l7 6 7-6" fill="none" stroke="#fff" stroke-width="1.2"/></svg>marcus@velora.com.hk</li>
      <li><svg viewBox="0 0 16 16"><circle cx="8" cy="8" r="6.5" fill="none" stroke="#5fb6c4" stroke-width="1.5"/><path d="M1.5 8h13M8 1.5c-3 3-3 10 0 13M8 1.5c3 3 3 10 0 13" fill="none" stroke="#5fb6c4" stroke-width="1.2"/></svg>www.velora.com.hk</li>
    </ul>
    <address class="address" style="font-style:normal">
      Unit 1820, 18th Floor<br>Harbour Point Tower<br>12 Kingsway Road, North Point
    </address>
  </section>

  <section class="card card-back">
    <div class="back-frame">
      <div class="branch-col">
        <div class="branch"><div class="branch-phone"><svg viewBox="0 0 16 16"><path d="M3 2l3 0 1 3-2 1.5c1 2 2.5 3.5 4.5 4.5L11 9l3 1v3c-6 1-12-5-11-11z" fill="#5fb6c4"/></svg>+65 5550 0101</div>28 Orchid Lane #03-11,<br>Bukit Rise, Singapore</div>
        <div class="branch"><div class="branch-phone"><svg viewBox="0 0 16 16"><path d="M3 2l3 0 1 3-2 1.5c1 2 2.5 3.5 4.5 4.5L11 9l3 1v3c-6 1-12-5-11-11z" fill="#5fb6c4"/></svg>+65 5550 0102</div>14 Marina Walk #01-05,<br>Bayfront, Singapore</div>
        <div class="branch"><div class="branch-phone"><svg viewBox="0 0 16 16"><path d="M3 2l3 0 1 3-2 1.5c1 2 2.5 3.5 4.5 4.5L11 9l3 1v3c-6 1-12-5-11-11z" fill="#5fb6c4"/></svg>+65 5550 0103</div>7 Cedar Street #02-18,<br>Tampines, Singapore</div>
        <div class="branch"><div class="branch-phone"><svg viewBox="0 0 16 16"><path d="M3 2l3 0 1 3-2 1.5c1 2 2.5 3.5 4.5 4.5L11 9l3 1v3c-6 1-12-5-11-11z" fill="#5fb6c4"/></svg>+65 5550 0104</div>51 Palm Avenue #01-22,<br>Jurong East, Singapore</div>
      </div>
      <div class="back-brand">
        <span class="brand-mark"></span>
        <div class="brand-name">VELORA</div>
        <div class="brand-sub">REMITTANCE AND<br>MONEY EXCHANGE</div>
      </div>
      <div class="branch-col">
        <div class="branch"><div class="branch-phone"><svg viewBox="0 0 16 16"><path d="M3 2l3 0 1 3-2 1.5c1 2 2.5 3.5 4.5 4.5L11 9l3 1v3c-6 1-12-5-11-11z" fill="#5fb6c4"/></svg>+65 5550 0105</div>3 Harbour Road #04-09,<br>Tiong Bahru, Singapore</div>
        <div class="branch"><div class="branch-phone"><svg viewBox="0 0 16 16"><path d="M3 2l3 0 1 3-2 1.5c1 2 2.5 3.5 4.5 4.5L11 9l3 1v3c-6 1-12-5-11-11z" fill="#5fb6c4"/></svg>+65 5550 0106</div>66 Lotus Drive #01-31,<br>Woodlands, Singapore</div>
        <div class="branch"><div class="branch-phone"><svg viewBox="0 0 16 16"><path d="M3 2l3 0 1 3-2 1.5c1 2 2.5 3.5 4.5 4.5L11 9l3 1v3c-6 1-12-5-11-11z" fill="#5fb6c4"/></svg>+65 5550 0107</div>19 Jade Crescent #02-07,<br>Serangoon, Singapore</div>
        <div class="branch"><div class="branch-phone"><svg viewBox="0 0 16 16"><path d="M3 2l3 0 1 3-2 1.5c1 2 2.5 3.5 4.5 4.5L11 9l3 1v3c-6 1-12-5-11-11z" fill="#5fb6c4"/></svg>+852 5550 0108</div>9 Kingsway Road,<br>North Point, Hong Kong</div>
      </div>
    </div>
  </section>

</main>
</body>
</html>
```